letter drop flyer

a6 flyer for letterdropping the suburb

I have attached my last one, so something along these lines but my phone number and business card is now different.

```html
<!DOCTYPE html>
<html lang="en">
<head>
<meta charset="utf-8">
<title>Ridgeway Realty – Clara Henshaw Letter Drop Flyer</title>
<link rel="stylesheet" href="https://fonts.googleapis.com/css2?family=Cormorant+Garamond:ital,wght@0,600;0,700;1,600;1,700&family=Arimo:ital,wght@0,400;1,400;1,700&display=swap">
<style>
  :root {
    --navy: #1b4580;
    --brand-blue: #1d62a8;
    --gold: #dcc792;
    --white: #ffffff;
    --red: #a3192a;
    --rule: #8aa0bf;
  }
  * { margin: 0; padding: 0; box-sizing: border-box; }
  html, body { width: 851px; height: 1200px; overflow: hidden; }
  body { background: var(--navy); }
  .flyer {
    position: relative;
    width: 851px;
    height: 1200px;
    background: var(--navy);
    overflow: hidden;
    color: var(--white);
  }
  .brand {
    position: absolute;
    left: 248px; top: 30px;
    width: 352px; height: 107px;
    background: var(--brand-blue);
    border-radius: 6px;
    display: flex; align-items: center; justify-content: center;
    font-family: "Arimo", Arial, sans-serif;
    font-weight: 400;
    font-size: 50px;
    letter-spacing: -1px;
    color: var(--white);
  }
  .agent-name {
    position: absolute;
    left: 0; right: 0; top: 178px;
    text-align: center;
    font-family: "Cormorant Garamond", Georgia, serif;
    font-weight: 600;
    font-size: 104px;
    line-height: 1;
    color: var(--gold);
  }
  .agent-role {
    position: absolute;
    right: 106px; top: 296px;
    font-family: "Cormorant Garamond", Georgia, serif;
    font-style: italic;
    font-weight: 700;
    font-size: 44px;
    line-height: 1;
    color: var(--white);
  }
  .acrostic { position: absolute; left: 0; top: 0; width: 100%; }
  .acrostic-item {
    position: absolute;
    left: 58px;
    display: flex;
    align-items: flex-start;
  }
  .drop-cap {
    width: 80px;
    font-family: "Cormorant Garamond", Georgia, serif;
    font-weight: 700;
    font-size: 92px;
    line-height: 0.8;
    color: var(--gold);
  }
  .item-text {
    margin-top: 2px;
    font-family: "Arimo", Arial, sans-serif;
    font-style: italic;
    font-size: 28px;
    line-height: 38px;
    color: var(--white);
  }
  .contact {
    position: absolute;
    right: 27px; top: 926px;
    text-align: right;
    font-family: "Arimo", Arial, sans-serif;
    font-size: 22px;
    line-height: 34px;
    color: var(--white);
  }
  .contact .tel { font-style: italic; }
  .rule {
    position: absolute;
    left: 0; top: 1065px;
    width: 100%; height: 3px;
    background: var(--rule);
  }
  .tagline-band {
    position: absolute;
    left: 0; top: 1068px;
    width: 100%; height: 132px;
    background: var(--red);
    display: flex; align-items: center; justify-content: center;
    font-family: "Cormorant Garamond", Georgia, serif;
    font-style: italic;
    font-weight: 700;
    font-size: 66px;
    color: var(--white);
  }
</style>
</head>
<body>
<main class="flyer">
  <div class="brand">Ridgeway Realty</div>

  <h1 class="agent-name">Clara Henshaw</h1>
  <p class="agent-role">Sales Executive</p>

  <section class="acrostic">
    <div class="acrostic-item" style="top:428px">
      <span class="drop-cap">F</span>
      <p class="item-text">or this week only I will be providing<br>FREE Market Estimates in your street</p>
    </div>
    <div class="acrostic-item" style="top:548px">
      <span class="drop-cap">R</span>
      <p class="item-text">ing your local area specialist Clara Henshaw<br>to arrange a convenient time</p>
    </div>
    <div class="acrostic-item" style="top:668px">
      <span class="drop-cap">E</span>
      <p class="item-text">stimates are completely FREE with<br>obligation what so ever</p>
    </div>
    <div class="acrostic-item" style="top:790px">
      <span class="drop-cap">E</span>
      <p class="item-text">very property will receive a written<br>portofolio of their market estimate</p>
    </div>
  </section>

  <address class="contact" style="font-style:normal">
    <div class="tel">Tel: 0400 271 846</div>
    <div>Web: www.ridgewayrealty.com.au</div>
    <div>Email: chenshaw@ridgewayrealty.com.au</div>
    <div>Adress: 418 Kestrel Road Norwood 6071</div>
  </address>

  <div class="rule"></div>
  <footer class="tagline-band">“You name it, I sell it”</footer>
</main>
</body>
</html>
```